Small but growing painting company. Have built up a steady client base. Want to start having a more professional look. Want to start with changing my business cards, and also getting new logo and tee shirts.

Target Market(s)

Home owners, property management companies, all ages 30-70

Industry/Entity Type

Painting And Decorating

Contact Information for Business Card

Bright Ridge Painting LLC Mark Delvecchi 630-584-3907 interior, exterior, vaulted ceiling, drywall repair, pressure washing, kitchen cabinets, epoxy, garage floors,

Font styles to use
Sans Serif
Other font styles liked:
• Harrington

Colors
0355a3
ffffff
ec1f27
000000
3176b5
0493ce
474747
b7b7b7

Requirements
Must have
• Creative, something that doesn’t look like every other painting card.
Nice to have
• I would like something with an arrow or something going to a point

```html
<!DOCTYPE html>
<html lang="en">
<head>
<meta charset="utf-8">
<title>Bright Ridge Painting LLC – Business Card</title>
<link rel="stylesheet" href="https://fonts.googleapis.com/css2?family=Arimo:wght@400;700&family=Questrial&display=swap">
<style>
  :root {
    --red: #ec1f27;
    --red-deep: #a8121a;
    --black: #111111;
    --card-light: #f4f4f4;
    --card-shade: #d9d9d9;
    --ink-soft: #f2e6e6;
    --page: #e6e6e6;
  }
  * { box-sizing: border-box; margin: 0; padding: 0; }
  html, body { width: 1200px; height: 970px; overflow: hidden; background: var(--page); }
  .canvas { position: relative; width: 1200px; height: 970px; }
  .card {
    position: absolute; left: 80px; top: 190px; width: 1040px; height: 590px;
    border-radius: 32px; overflow: hidden;
    background: linear-gradient(160deg, var(--card-light), var(--card-shade));
    box-shadow: 0 10px 30px rgba(0,0,0,.18);
    font-family: "Arimo", Arial, sans-serif;
  }
  .band { position: absolute; inset: 0; width: 1040px; height: 590px; }
  .brand { position: absolute; left: 60px; top: 112px; display: flex; align-items: center; gap: 30px; }
  .brand-dot { width: 96px; height: 96px; border-radius: 50%; background: var(--red); }
  .brand-name { font-family: "Questrial", sans-serif; color: var(--black); line-height: 1; }
  .brand-name .line-main { display: block; font-size: 62px; }
  .brand-name .line-sub { display: block; font-size: 34px; letter-spacing: 10px; margin-top: 8px; }
  .person { position: absolute; right: 58px; top: 78px; text-align: right; }
  .person-name { font-size: 34px; font-weight: 700; color: var(--black); }
  .person-role { font-size: 25px; color: var(--red); margin-top: 4px; }
  .address { position: absolute; right: 58px; top: 355px; text-align: right; color: var(--ink-soft); font-size: 25px; line-height: 33px; }
  .contacts { position: absolute; right: 56px; top: 444px; list-style: none; }
  .contacts li { display: flex; justify-content: flex-end; align-items: center; gap: 12px; height: 35px; color: var(--ink-soft); font-size: 24px; }
  .contacts svg { width: 30px; height: 30px; }
</style>
</head>
<body>
<div class="canvas">
  <div class="card">
    <svg class="band" viewBox="0 0 1040 590" preserveAspectRatio="none" role="img" aria-label="Decorative red and black swoosh across the lower card">
      <defs>
        <linearGradient id="bandFill" x1="0" y1="0" x2="1" y2="1">
          <stop offset="0" stop-color="#ec1f27"/>
          <stop offset="1" stop-color="#a8121a"/>
        </linearGradient>
      </defs>
      <path d="M0 470 C 320 500, 620 320, 1040 282 L1040 590 L0 590 Z" fill="url(#bandFill)"/>
    </svg>

    <div class="brand">
      <span class="brand-dot"></span>
      <span class="brand-name">
        <span class="line-main">Bright Ridge</span>
        <span class="line-sub">Painting LLC</span>
      </span>
    </div>

    <div class="person">
      <div class="person-name">MARK DELVECCHI</div>
      <div class="person-role">President &amp; CEO</div>
    </div>

    <div class="address">
      PO BOX 418, Oak Street<br>2nd Lane, Naperville
    </div>

    <ul class="contacts">
      <li>630-584-3907
        <svg viewBox="0 0 30 30" aria-hidden="true"><circle cx="15" cy="15" r="13" fill="none" stroke="#f2e6e6" stroke-width="2"/><path d="M9 11 C9 9 21 9 21 11 L19 13 L17 12 L13 12 L11 13 Z M10 15 H20 V21 H10 Z" fill="#f2e6e6"/></svg>
      </li>
      <li>info@brightridgepaint.com
        <svg viewBox="0 0 30 30" aria-hidden="true"><circle cx="15" cy="15" r="13" fill="none" stroke="#f2e6e6" stroke-width="2"/><rect x="8" y="10" width="14" height="10" fill="none" stroke="#f2e6e6" stroke-width="2"/><path d="M8 10 L15 16 L22 10" fill="none" stroke="#f2e6e6" stroke-width="2"/></svg>
      </li>
      <li>www.brightridgepaint.com
        <svg viewBox="0 0 30 30" aria-hidden="true"><circle cx="15" cy="15" r="13" fill="none" stroke="#f2e6e6" stroke-width="2"/><circle cx="15" cy="15" r="7" fill="none" stroke="#f2e6e6" stroke-width="1.5"/><path d="M8 15 H22 M15 8 C11 12 11 18 15 22 M15 8 C19 12 19 18 15 22" fill="none" stroke="#f2e6e6" stroke-width="1.5"/></svg>
      </li>
    </ul>
  </div>
</div>
</body>
</html>
```